"The Craft of Patron Care," fourth edition cover design

Later this year, my publisher, Harold Penmarsh & Daughters, will issue a fourth, substantially revised edition of "The Craft of Patron Care," following the 2016 publication of the third edition and the second and first versions that were issued earlier.

To distinguish this new edition from previous ones, I need a cover design that visually connects and is consistent with what has preceded it, while signaling this is a new and different, worthy of prospective readers/buyers’ attention.

Attached are three different verbal approaches to the new cover; these are NOT MEANT to serve as actual designs, but rather will give you a sense of how language is to be deployed:

The first emphasizes “ART” as the key visual word in the book title;
The second emphasizes “CLIENT SERVICE” as the key visual words in the book title; and,
The third emphasizes just the word "CLIENT" in the book title.

A top-of-the-page is a pre-head that applies to all three versions:
“6 TIMELESS PRINCIPLES FOR ADVERTISING & MARKETING PRO’s
IN AN AI WORLD"

There's a mid-page sub-head for all three versions:
“THE CLASSIC GUIDE,” followed by
“FOURTH EDITION BY GERALD ASHCOMBE

And there's a one-line, bottom-of-the-page designation:
“Foreword by Mae Dunford, Global Executive Creative Director, Starbolt"

The pallette for the previously published third edition was black with red as an accent color on a field of white; I've attached a sample for reference, so you can see how it was executed. For this new fourth edition, I'd like to change the accent color from red to either Wedgewood blue, or British racing green, or an alternative that is assertive and color saturated -- think of primary colors -- that contrast sufficiently with the base of black. As an alternative, you can consider a cover that used either Wedgewood blue, British racing green, or another possibility as a full-bleed field, with copy content either revered out or surprinted.

Lastly, while the new cover largely is meant to be typographically driven, if you can come up with a visual metaphor that illustrates and builds on the book's title, that would be very helpful. By way of reference, the third edition's book cover attempted to do this by introducing a visual element at the end of the book's title that's meant to represent an artist's paint splatter (although I admit it didn't work as well as it should).

Target Market(s)

Prospective purchasers of the book who might discover copies at a bookstore, but more likely will encounter it through online distributors such as Riverdex, Hartwell & Pike, and Tindall’s.

Industry/Entity Type

Advertising and marketing

Font styles to use
Serif
Sans Serif
Other font styles liked:
• A mix of serif and san-serif typefaces is okay. for the examples I shared, I relieid on "Arial Rounded Bold" but you need not be weeded to this. If you opt to mix in a serif font, I am partial to Cambria as a typeface.

Requirements
Must have
• To achieve the goal of being “connected with but distinct” from previous editions, the new cover should be:  Largely typographic, but displaying a color palette different from the previous editions’ black-plus-red-accent on a canvas of white.  Any new accent color selected for use should be vibrant, strong, and highly saturated; think “British racing green,” “Wedgewood blue,” or their equivalents.  In addition to a powerful, “billboard” approach to type and color, consider other visual metaphors that are likely to engage the readers. The winning cover design will stand out from other books, while connecting with the previously published third edition.
Nice to have
• If you can find way to illustrate the book's title through a visual metaphor, that would be ideal.a
Should not have
• Anything that is frivolous or non-sensical

```html
<!DOCTYPE html>
<html lang="en">
<head>
<meta charset="utf-8">
<title>The Craft of Patron Care — Fourth Edition Cover</title>
<link rel="stylesheet" href="https://fonts.googleapis.com/css2?family=Bodoni+Moda:ital,opsz,wght@0,6..96,400;0,6..96,500;1,6..96,500;1,6..96,700&family=Libre+Baskerville:wght@400;700&display=swap">
<style>
  :root {
    --ink: #0b0b0e;
    --accent-red: #cc5248;
    --accent-blue: #8d98cf;
    --paper: #f1eee8;
  }
  * { margin: 0; padding: 0; box-sizing: border-box; }
  html, body { width: 800px; height: 1200px; overflow: hidden; background: var(--ink); }
  .cover {
    position: relative;
    width: 800px;
    height: 1200px;
    background: var(--ink);
    overflow: hidden;
    font-family: "Bodoni Moda", "Libre Baskerville", serif;
  }
  .rule { position: absolute; }
  .rule--red { background: var(--accent-red); }
  .rule--blue { background: var(--accent-blue); }
  .rule--v { width: 3px; }
  .rule--h { height: 3px; }

  .prehead {
    position: absolute;
    left: 372px; top: 26px;
    width: 418px; height: 104px;
    border: 2px solid var(--accent-red);
    display: flex; flex-direction: column; justify-content: center; align-items: center;
    color: var(--paper);
    font-family: "Libre Baskerville", serif;
    font-size: 15px;
    line-height: 1.4;
    letter-spacing: 0.03em;
    text-transform: uppercase;
    text-align: center;
    white-space: nowrap;
  }

  .title { position: absolute; line-height: 1; white-space: nowrap; }
  .title__the {
    left: 200px; top: 362px;
    font-size: 62px; font-weight: 500;
    color: var(--accent-blue); letter-spacing: 0.02em;
  }
  .title__craft {
    left: 400px; top: 318px;
    font-size: 104px; font-weight: 500;
    color: var(--accent-red); letter-spacing: -0.01em;
  }
  .title__of {
    left: 272px; top: 536px;
    font-size: 56px; font-weight: 500;
    color: var(--accent-red);
  }
  .title__patron, .title__care {
    left: 402px;
    font-size: 84px; font-weight: 500;
    color: var(--accent-blue);
    letter-spacing: 0.01em;
  }
  .title__patron { top: 496px; }
  .title__care { top: 590px; }

  .edition { position: absolute; left: 48px; top: 700px; }
  .edition__label {
    font-family: "Libre Baskerville", serif;
    font-size: 27px; color: var(--paper); letter-spacing: 0.02em;
  }
  .edition__number {
    font-family: "Libre Baskerville", serif;
    font-size: 19px; font-weight: 700;
    color: var(--accent-red); letter-spacing: 0.04em;
    text-align: right; margin-top: 4px;
  }

  .credits {
    position: absolute; right: 52px; top: 990px;
    text-align: right;
  }
  .author {
    font-style: italic; font-weight: 700;
    font-size: 32px; line-height: 1.1; color: var(--accent-red); letter-spacing: 0.03em;
    white-space: nowrap;
  }
  .foreword {
    margin-top: 8px;
    font-style: italic; font-weight: 500;
    font-size: 17px; line-height: 1.3; color: var(--paper);
    white-space: nowrap;
  }

  .stars { position: absolute; left: 8px; top: 1110px; }
  .star--red { fill: var(--accent-red); }
  .star--blue { fill: var(--accent-blue); }
</style>
</head>
<body>
<main class="cover">
  <div class="rule rule--red rule--v" style="left:128px; top:0; height:560px;"></div>
  <div class="rule rule--red rule--v" style="left:385px; top:0; height:26px;"></div>
  <div class="rule rule--red rule--v" style="left:385px; top:132px; height:346px;"></div>
  <div class="rule rule--blue rule--h" style="left:0; top:507px; width:387px;"></div>
  <div class="rule rule--red rule--v" style="left:385px; top:480px; height:330px;"></div>
  <div class="rule rule--blue rule--h" style="left:385px; top:480px; width:415px;"></div>
  <div class="rule rule--red rule--h" style="left:0; top:690px; width:128px;"></div>

  <p class="prehead">6 Timeless principles for<br>advertising &amp; marketing pros in<br>an A.I. world</p>

  <h1>
    <span class="title title__the">THE</span>
    <span class="title title__craft">CRAFT</span>
    <span class="title title__of">OF</span>
    <span class="title title__patron">PATRON</span>
    <span class="title title__care">CARE</span>
  </h1>

  <div class="edition">
    <p class="edition__label">THE CLASSIC GUIDE</p>
    <p class="edition__number">FOURTH EDITION</p>
  </div>

  <div class="credits">
    <p class="author">GERALD ASHCOMBE</p>
    <p class="foreword">Foreword by Mae Dunford, Global Executive<br>Creative Director, Starbolt</p>
  </div>

  <svg class="stars" width="380" height="70" viewBox="0 0 380 70" aria-hidden="true">
    <defs>
      <polygon id="star" points="35,2 43,26 68,26 48,41 55,66 35,51 15,66 22,41 2,26 27,26"/>
    </defs>
    <use href="#star" class="star--red" x="0"/>
    <use href="#star" class="star--blue" x="74"/>
    <use href="#star" class="star--red" x="148"/>
    <use href="#star" class="star--blue" x="222"/>
    <use href="#star" class="star--red" x="296"/>
  </svg>
</main>
</body>
</html>
```